Change consultancy needs business card+ design

We need business card design for a Seattle based consulting firm called
Holloway + Brine. Our firm helps organizations shift their paradigms, lean into change, and reimagine the way they work together.
**Updated**
Our firm name is the logo using black and orange font, see attached. We would like to include the tagline "(Re)imagining how people work"
The final design should find a balance between playful, edgy and professional. For example, we are using the attached goldfish photo on our homepage and like the colors and concept of leaping forward. However, don't want to use the image on the card.
Lastly, depending on the winning design, we will also be looking for stationary/template design that will compliment the business card.
Industry/Entity Type
Business
Font styles to use
Other font styles liked:
- Helvetica
Look and feel
Each slider illustrates characteristics of the customer's brand and the style your logo design should communicate.

```html
<!DOCTYPE html>
<html lang="en">
<head>
<meta charset="utf-8">
<title>Holloway + Brine — Business Card, Proposal 3</title>
<link rel="stylesheet" href="https://fonts.googleapis.com/css2?family=Roboto+Condensed:wght@300;700&family=Roboto:wght@300&display=swap">
<style>
  :root {
    --ink: #231f20;
    --paper: #ffffff;
    --accent: #f26522;
    --label: #231f20;
  }
  html, body {
    margin: 0;
    padding: 0;
    width: 1030px;
    height: 1200px;
    overflow: hidden;
    background: var(--paper);
  }
  .sheet {
    position: relative;
    width: 1030px;
    height: 1200px;
  }
  .sheet-svg {
    display: block;
    width: 1030px;
    height: 1200px;
  }
  .proposal-label {
    font-family: "Roboto Condensed", "Arial Narrow", sans-serif;
    font-weight: 300;
    font-size: 30px;
    fill: var(--label);
  }
  .card-face { fill: var(--ink); }
  .cross-arm {
    stroke: var(--paper);
    stroke-width: 96;
    stroke-linecap: butt;
    fill: none;
  }
  .contact-panel { fill: var(--paper); }
  .name-bold {
    font-family: "Roboto Condensed", "Arial Narrow", sans-serif;
    font-weight: 700;
    font-size: 52px;
    fill: var(--ink);
    dominant-baseline: central;
  }
  .name-bold.is-accent { fill: var(--accent); }
  .line-light {
    font-family: "Roboto", "Helvetica Neue", Arial, sans-serif;
    font-weight: 300;
    font-size: 24px;
    fill: var(--ink);
    dominant-baseline: central;
  }
  .contact-text {
    font-family: "Roboto", "Helvetica Neue", Arial, sans-serif;
    font-weight: 300;
    font-size: 21px;
    fill: var(--ink);
  }
  .tagline {
    font-family: "Roboto", "Helvetica Neue", Arial, sans-serif;
    font-weight: 300;
    font-size: 26px;
    fill: var(--accent);
    letter-spacing: 0.5px;
  }
</style>
</head>
<body>
<main class="sheet">
  <svg class="sheet-svg" viewBox="0 0 1285 1500" xmlns="http://www.w3.org/2000/svg">
    <text class="proposal-label" x="118" y="72">Proposal 3</text>

    <!-- Back of card -->
    <g class="card card-back">
      <rect class="card-face" x="118" y="118" width="1051" height="602"/>
      <line class="cross-arm" x1="643" y1="720" x2="391" y2="471"/>
      <line class="cross-arm" x1="643" y1="720" x2="893" y2="470"/>

      <polygon class="contact-panel" points="571,147 827,405 641,589 385,333"/>
      <g class="contact-block" transform="translate(606 368) rotate(135)">
        <text class="contact-text" x="-112" y="-142">United States</text>
        <text class="contact-text" x="-112" y="-117">Street Address, Building</text>
        <text class="contact-text" x="-112" y="-92">ZIP CODE</text>
        <text class="contact-text" x="-112" y="-40">+ 1 000 55 66</text>
        <text class="contact-text" x="-112" y="-15">+ 1 000 33 88</text>
        <text class="contact-text" x="-112" y="38">holloway+brine.com</text>
        <text class="contact-text" x="-112" y="63">h.w@host.com</text>
      </g>

      <text class="line-light" transform="translate(643 720) rotate(45)" x="-331" y="6">Holloway+Brine, LLC</text>
      <text class="name-bold is-accent" transform="translate(643 720) rotate(-45)" x="124" y="2">Brine</text>
    </g>

    <!-- Front of card -->
    <g class="card card-front">
      <rect class="card-face" x="118" y="780" width="1051" height="602"/>
      <line class="cross-arm" x1="643" y1="780" x2="395" y2="1030"/>
      <line class="cross-arm" x1="643" y1="780" x2="895" y2="1030"/>

      <text class="name-bold" transform="translate(643 780) rotate(-45)" x="-88" y="-2" text-anchor="end">Holloway</text>
      <text class="line-light" transform="translate(643 780) rotate(45)" x="44" y="4">Consultants</text>

      <text class="tagline" x="643" y="1300" text-anchor="middle">(Re)imagining how people work</text>
    </g>
  </svg>
</main>
</body>
</html>
```